Japanese Rice Food Package Label

- We are launching Japanese food products to the outdoor community.
- Made in Japan
- We will have multiple flavors of rice but want to keep the package label almost the same and only replace the flavor text (e.g., Mixed Rice, Curry Rice, etc)
- We like simple designs inspired by Japan.
- Label size: 105 mm x148 mm
- Our brand: YOBEN https://yoben.co/
- Video message: https://www.vidqo.com/share/3f51b07a9e2c4d6891a0c7e5b2d94f18

```html
<!DOCTYPE html>
<html lang="en">
<head>
<meta charset="utf-8">
<title>YOBEN Mixed Rice Pouch Label</title>
<link rel="stylesheet" href="https://fonts.googleapis.com/css2?family=Montserrat:wght@500;800;900&family=Noto+Sans+JP:wght@500&display=swap">
<style>
  :root {
    --page: #ffffff;
    --pouch-line: #3a3a3a;
    --label-cream: #faf5d0;
    --olive: #828b45;
    --sun-red: #e8202a;
    --ink: #0b0b0b;
    --date-ink: #444444;
  }
  html, body {
    margin: 0;
    padding: 0;
    width: 1200px;
    height: 1200px;
    overflow: hidden;
    background: var(--page);
  }
  .canvas {
    position: relative;
    width: 1200px;
    height: 1200px;
  }
  .pouch-art {
    position: absolute;
    inset: 0;
    width: 1200px;
    height: 1200px;
  }
  .pouch-outline { fill: var(--page); stroke: var(--pouch-line); stroke-width: 1.4; }
  .hang-hole { fill: none; stroke: var(--pouch-line); stroke-width: 1.6; }
  .label-panel { fill: var(--label-cream); }
  .mountain-illustration { fill: var(--olive); }
  .origin-dot { fill: var(--sun-red); }
  .origin-text {
    font-family: "Montserrat", sans-serif;
    font-weight: 500;
    font-size: 15px;
    letter-spacing: 4.6px;
    fill: var(--sun-red);
  }
  .flavor-name {
    font-family: "Montserrat", sans-serif;
    font-weight: 800;
    font-size: 56px;
    fill: var(--olive);
  }
  .brand-name {
    font-family: "Montserrat", sans-serif;
    font-weight: 900;
    font-size: 148px;
    fill: var(--ink);
  }
  .best-before {
    font-family: "Noto Sans JP", sans-serif;
    font-weight: 500;
    font-size: 14px;
    fill: var(--date-ink);
  }
</style>
</head>
<body>
<main class="canvas">
  <svg class="pouch-art" viewBox="0 0 1200 1200" xmlns="http://www.w3.org/2000/svg">
    <path class="pouch-outline" d="M246 292 H988 Q1018 292 1018 322 V372 Q1018 384 1008 392 Q1004 398 1008 406 Q1014 414 1014 430 V976 Q1014 1012 978 1018 Q810 1034 600 1034 Q390 1034 222 1018 Q220 1018 220 1010 Q222 990 222 976 V430 Q222 414 228 406 Q232 398 228 392 Q216 384 216 372 V322 Q216 292 246 292 Z"/>
    <rect class="hang-hole" x="594" y="311" width="40" height="25" rx="10"/>
    <text class="best-before" x="822" y="332">賞味期限2026.08</text>

    <rect class="label-panel" x="376" y="458" width="602" height="518"/>
    <polygon class="mountain-illustration" role="img" aria-label="Illustration of a sprout beneath a red sun inside a mountain shape" points="613,612 978,976 376,976 376,850"/>

    <circle class="origin-dot" cx="402" cy="477" r="7"/>
    <text class="origin-text" x="418" y="483">MADE IN JAPAN</text>

    <text class="brand-name" transform="translate(954 962) rotate(-90)" textLength="450" lengthAdjust="spacingAndGlyphs">YOBEN</text>

    <text class="flavor-name" transform="translate(325 976) rotate(-90)">mixed rice</text>
  </svg>
</main>
</body>
</html>
```